North Fern Holdings Business Card

A business card design to accompany the logo design you completed on Artisan Hive. We are open to your proposals. I did add one idea below that might work, but we aren't married to the idea. The company is a real estate services company. Clientele are typically high net worth individuals, executive level employment or owners of their own company, 30-60 years old.

Our 1 (bad?) idea: double sided card; One side landscape with logo and word mark. Other side Portrait with the logo only (oversize watermark maybe?). Somewhere add text of Name (Marcus Pellington), Title (Principal), phone # (949-555-0173) and email address (marcus@northfernhq.com). There would be a second design with my wife's name, number and email in place of mine.

Again totally open to ideas here.

Industry/Entity Type

Real Estate

```html
<!DOCTYPE html>
<html lang="en">
<head>
<meta charset="utf-8">
<title>North Fern Holdings – Business Card Options</title>
<link rel="stylesheet" href="https://fonts.googleapis.com/css2?family=Cinzel:wght@400;600&family=Arimo:wght@400&family=Source+Sans+3:wght@400&display=swap">
<style>
  :root {
    --sage: #629f55;
    --sage-pale: #a9cc9f;
    --paper: #ffffff;
    --stage-top: #5c5c5c;
    --stage-bottom: #7a7a7a;
    --divider: #8c8c8c;
    --label: #e6e6e6;
    --grey-word: #8a8a8a;
  }
  * { margin: 0; padding: 0; box-sizing: border-box; }
  html, body { width: 1200px; height: 1000px; overflow: hidden; }
  body { background: var(--stage-top); font-family: "Arimo", Arial, sans-serif; position: relative; }

  .option-section { position: absolute; left: 0; width: 1200px; }
  .option-section--one { top: 0; height: 492px; background: var(--stage-top); }
  .option-section--two { top: 492px; height: 508px; background: var(--stage-bottom); border-top: 3px solid var(--divider); }

  .option-label {
    position: absolute; font-family: "Source Sans 3", sans-serif;
    font-size: 26px; color: var(--label); letter-spacing: 0.5px;
  }

  .card { position: absolute; overflow: hidden; box-shadow: 0 3px 8px rgba(0,0,0,0.35); }
  .card--landscape { width: 378px; height: 232px; }
  .card--portrait { width: 232px; height: 378px; }

  .wordmark { font-family: "Cinzel", serif; font-weight: 400; line-height: 1; display: flex; align-items: center; gap: 12px; }
  .wordmark__dot { width: 14px; height: 14px; border-radius: 50%; flex: none; }

  .web-band {
    position: absolute; left: 0; right: 0; height: 12px;
    display: flex; align-items: center; justify-content: center; gap: 4px;
    font-size: 9px;
  }
  .web-band svg { width: 8px; height: 8px; }

  .person { position: absolute; left: 0; right: 0; text-align: center; }
  .person__name { font-family: "Cinzel", serif; font-size: 16px; font-weight: 600; }
  .person__title { font-size: 10px; margin-top: 6px; }
  .contact { position: absolute; left: 0; right: 0; text-align: center; font-size: 10px; line-height: 15px; }
  .contact__row { display: flex; justify-content: center; align-items: center; gap: 4px; }
  .contact svg { width: 8px; height: 9px; }

  /* Option 1 */
  .o1-front { left: 37px; top: 43px; background: var(--sage); border: 1px solid rgba(0,0,0,0.2); }
  .o1-front .wordmark { position: absolute; left: 68px; top: 78px; color: var(--paper); font-size: 26px; }
  .o1-front .wordmark__dot { background: var(--paper); }
  .o1-front .web-band { top: 161px; left: 2px; right: 2px; background: var(--paper); color: var(--sage); }

  .o1-back { left: 453px; top: 43px; background: var(--sage); }
  .o1-back__head { position: absolute; left: 0; top: 0; width: 100%; height: 120px; background: var(--paper); }
  .o1-back .wordmark { position: absolute; left: 0; right: 0; top: 50px; justify-content: center; font-size: 14px; color: var(--sage); gap: 6px; }
  .o1-back .wordmark__dot { background: var(--sage); width: 9px; height: 9px; }
  .o1-back .person { top: 150px; color: var(--paper); }
  .o1-back .contact { top: 304px; color: var(--paper); }

  /* Option 2 */
  .o2-front { left: 508px; top: 219px; background: var(--paper); }
  .o2-front .wordmark { position: absolute; left: 0; right: 0; top: 70px; justify-content: center; color: var(--sage); font-size: 25px; }
  .o2-front .wordmark__dot { background: var(--sage); }
  .o2-front .web-band { top: 160px; background: var(--sage); color: var(--paper); }

  .o2-back { left: 913px; top: 72px; width: 245px; background: var(--paper); }
  .o2-back__field { position: absolute; left: 0; top: 0; width: 100%; height: 240px; background: var(--sage); }
  .o2-back__emblem { position: absolute; left: 32px; top: 40px; width: 180px; height: 180px; }
  .o2-back .person { top: 262px; color: var(--sage); }
  .o2-back .person__title { color: #555; }
  .o2-back .contact { top: 330px; color: var(--sage); }
</style>
</head>
<body>

<section class="option-section option-section--one">
  <div class="card card--landscape o1-front">
    <div class="wordmark"><span class="wordmark__dot"></span>North Fern Holdings</div>
    <div class="web-band">
      <svg viewBox="0 0 10 10"><circle cx="5" cy="5" r="4.3" fill="none" stroke="currentColor" stroke-width="1.2"/><path d="M1 5h8M5 1c-2 2-2 6 0 8M5 1c2 2 2 6 0 8" fill="none" stroke="currentColor" stroke-width="0.8"/></svg>
      www.northfernhq.com
    </div>
  </div>

  <div class="card card--portrait o1-back">
    <div class="o1-back__head"></div>
    <div class="wordmark"><span class="wordmark__dot"></span>North Fern Holdings</div>
    <div class="person">
      <div class="person__name">Marcus Pellington</div>
      <div class="person__title">Principal</div>
    </div>
    <div class="contact">
      <div class="contact__row"><svg viewBox="0 0 8 10"><rect x="1" y="0.5" width="6" height="9" rx="1" fill="none" stroke="currentColor"/></svg>949-555-0173</div>
      <div class="contact__row"><svg viewBox="0 0 10 9"><rect x="0.5" y="1.5" width="9" height="6.5" fill="none" stroke="currentColor"/><path d="M0.5 1.5l4.5 3.5 4.5-3.5" fill="none" stroke="currentColor"/></svg>marcus@northfernhq.com</div>
    </div>
  </div>

  <div class="option-label" style="left:156px; top:300px;">Option 1</div>
</section>

<section class="option-section option-section--two">
  <div class="option-label" style="left:646px; top:86px;">Option 2</div>

  <div class="card card--landscape o2-front">
    <div class="wordmark"><span class="wordmark__dot"></span>North Fern Holdings</div>
    <div class="web-band">
      <svg viewBox="0 0 10 10"><circle cx="5" cy="5" r="4.3" fill="none" stroke="currentColor" stroke-width="1.2"/><path d="M1 5h8M5 1c-2 2-2 6 0 8M5 1c2 2 2 6 0 8" fill="none" stroke="currentColor" stroke-width="0.8"/></svg>
      www.northfernhq.com
    </div>
  </div>

  <div class="card card--portrait o2-back">
    <div class="o2-back__field"></div>
    <svg class="o2-back__emblem" viewBox="0 0 180 180" role="img" aria-label="Large faint brand mark area">
      <circle cx="90" cy="90" r="86" fill="var(--sage-pale)" opacity="0.55"/>
    </svg>
    <div class="person">
      <div class="person__name">Marcus Pellington</div>
      <div class="person__title">Principal</div>
    </div>
    <div class="contact">
      <div class="contact__row"><svg viewBox="0 0 8 10"><rect x="1" y="0.5" width="6" height="9" rx="1" fill="none" stroke="currentColor"/></svg>949-555-0173</div>
      <div class="contact__row"><svg viewBox="0 0 10 9"><rect x="0.5" y="1.5" width="9" height="6.5" fill="none" stroke="currentColor"/><path d="M0.5 1.5l4.5 3.5 4.5-3.5" fill="none" stroke="currentColor"/></svg>marcus@northfernhq.com</div>
    </div>
  </div>
</section>

</body>
</html>
```